Bref créative
Brightpath Outcomes Inc
I need double sided standard sized Business Card [3.5" x 2"]
You decid
Professional
Danielle Hartwell
CEO
4172 Juniper Ridge Drive,
Suite 517
Cedar Hollow, MI 48109
danielle.hartwell@brightpathoutcomes.example
www.brightpathoutcomes.example
On the back of the card we want another web adrdress of
steadystepsforward.example

```html
<!DOCTYPE html>
<html lang="en">
<head>
<meta charset="utf-8">
<title>Brightpath Outcomes Inc — Stationery Set</title>
<link rel="stylesheet" href="https://fonts.googleapis.com/css2?family=Roboto:wght@400;700&display=swap">
<style>
  :root {
    --bg: #e9e6e2;
    --red: #e4242b;
    --red-light: #f26a5f;
    --black: #141414;
    --paper: #ffffff;
    --ink: #333333;
    --muted: #777777;
  }
  * { box-sizing: border-box; margin: 0; padding: 0; }
  html, body { width: 1200px; height: 701px; overflow: hidden; }
  body { background: var(--bg); font-family: "Roboto", Arial, sans-serif; color: var(--ink); position: relative; }
  .piece { position: absolute; background: var(--paper); box-shadow: 0 4px 14px rgba(0,0,0,.18); overflow: hidden; }
  .piece svg.wave { position: absolute; left: 0; width: 100%; display: block; }
  .brand { position: absolute; display: flex; align-items: center; gap: 6px; background: var(--paper); border-radius: 3px; padding: 5px 9px; }
  .brand-mark { width: 14px; height: 14px; background: var(--black); flex: none; }
  .brand-name { font-weight: 700; color: var(--black); text-transform: uppercase; line-height: 1.05; white-space: nowrap; }
  .fine { position: absolute; color: var(--muted); font-size: 7px; line-height: 1.35; white-space: nowrap; }

  /* envelope back */
  .envelope-back { left: 79px; top: 115px; width: 377px; height: 305px; z-index: 1; }
  .envelope-back .flap { position: absolute; left: 0; top: 0; width: 100%; height: 100%; }
  .envelope-back .brand { left: 160px; top: 40px; }
  .envelope-back .brand-name { font-size: 9px; }
  .envelope-back .fine { left: 0; right: 0; top: 160px; text-align: center; color: #fbd3cf; }

  /* letterhead */
  .letterhead { left: 470px; top: 17px; width: 413px; height: 583px; z-index: 2; }
  .letterhead .wave { top: 0; height: 110px; }
  .letterhead .brand { left: 14px; top: 30px; }
  .letterhead .brand-name { font-size: 11px; }
  .letterhead .fine { left: 14px; right: 14px; bottom: 7px; font-size: 5.5px; }
  .letterhead .foot-rule { position: absolute; left: 0; right: 0; bottom: 0; height: 4px; background: var(--red); }

  /* envelope front */
  .envelope-front { left: 144px; top: 336px; width: 449px; height: 259px; z-index: 3; }
  .envelope-front .wave { top: 0; height: 85px; }
  .envelope-front .brand { left: 10px; top: 18px; }
  .envelope-front .brand-name { font-size: 10px; }
  .envelope-front .fine { left: 32px; top: 86px; color: var(--ink); }
  .envelope-front .foot-rule { position: absolute; left: 0; right: 0; bottom: 0; height: 5px; background: var(--red); }

  /* business cards */
  .card-back { left: 902px; top: 288px; width: 132px; height: 209px; background: var(--black); }
  .card-back .red-panel { position: absolute; left: 0; top: 0; width: 100%; height: 104px; background: linear-gradient(180deg, var(--red-light), var(--red)); }
  .card-back .fine { left: 0; right: 0; text-align: center; font-size: 5.5px; }
  .card-back .web-red { top: 48px; color: #fde0dc; }
  .card-back .web-dark { top: 152px; color: #cfcfcf; }

  .card-front { left: 902px; top: 504px; width: 132px; height: 115px; }
  .card-front .wave { top: 0; height: 44px; }
  .card-front .brand { left: 30px; top: 26px; padding: 3px 5px; gap: 4px; }
  .card-front .brand-mark { width: 8px; height: 8px; }
  .card-front .brand-name { font-size: 6px; }
  .card-front .person { position: absolute; right: 6px; top: 62px; text-align: right; }
  .card-front .person-name { font-size: 7px; font-weight: 700; color: var(--red); }
  .card-front .person-title { font-size: 5.5px; color: var(--ink); }
  .card-front .fine { left: 6px; top: 80px; font-size: 4.6px; }
</style>
</head>
<body>

<section class="piece envelope-back">
  <svg class="flap" viewBox="0 0 377 305" preserveAspectRatio="none" aria-hidden="true">
    <path d="M0 0 H377 V120 L188 30 L0 120 Z" fill="#f4f4f4"/>
    <path d="M0 110 L188 190 L377 110 V195 H0 Z" fill="var(--red)"/>
    <path d="M0 110 L188 190 L377 110" fill="none" stroke="#d6d6d6" stroke-width="1"/>
  </svg>
  <div class="brand"><span class="brand-mark"></span><span class="brand-name">Brightpath<br>Outcomes</span></div>
  <p class="fine">www.brightpathoutcomes.example</p>
</section>

<section class="piece letterhead">
  <svg class="wave" viewBox="0 0 413 110" preserveAspectRatio="none" aria-hidden="true">
    <path d="M0 0 H413 V20 C330 22 270 60 200 70 C120 82 50 70 0 60 Z" fill="var(--red)"/>
    <path d="M200 72 C270 62 330 26 413 24 V36 C330 40 280 74 200 84 C140 92 80 88 40 80 C100 84 150 80 200 72 Z" fill="var(--black)"/>
  </svg>
  <div class="brand"><span class="brand-mark"></span><span class="brand-name">Brightpath<br>Outcomes</span></div>
  <p class="fine">4172 Juniper Ridge Drive, Suite 517, Cedar Hollow, MI 48109 &nbsp;|&nbsp; danielle.hartwell@brightpathoutcomes.example &nbsp;|&nbsp; www.brightpathoutcomes.example</p>
  <div class="foot-rule"></div>
</section>

<section class="piece envelope-front">
  <svg class="wave" viewBox="0 0 449 85" preserveAspectRatio="none" aria-hidden="true">
    <path d="M0 0 H449 V48 C340 86 240 40 150 60 C90 72 40 68 0 58 Z" fill="var(--red)"/>
    <path d="M150 62 C240 42 340 88 449 52 V60 C340 94 240 52 150 70 C110 78 70 78 40 74 C80 72 110 70 150 62 Z" fill="var(--black)"/>
  </svg>
  <div class="brand"><span class="brand-mark"></span><span class="brand-name">Brightpath<br>Outcomes</span></div>
  <p class="fine">4172 Juniper Ridge Drive, Suite 517<br>Cedar Hollow, MI 48109</p>
  <div class="foot-rule"></div>
</section>

<section class="piece card-back">
  <div class="red-panel"></div>
  <p class="fine web-red">www.brightpathoutcomes.example</p>
  <p class="fine web-dark">steadystepsforward.example</p>
</section>

<section class="piece card-front">
  <svg class="wave" viewBox="0 0 132 44" preserveAspectRatio="none" aria-hidden="true">
    <path d="M0 0 H132 V14 C100 16 80 34 50 36 C30 38 14 34 0 30 Z" fill="var(--red)"/>
    <path d="M50 37 C80 35 100 18 132 16 V22 C100 26 82 42 50 42 C34 42 20 40 10 37 C26 39 38 38 50 37 Z" fill="var(--black)"/>
  </svg>
  <div class="brand"><span class="brand-mark"></span><span class="brand-name">Brightpath<br>Outcomes</span></div>
  <div class="person">
    <p class="person-name">Danielle Hartwell</p>
    <p class="person-title">CEO</p>
  </div>
  <p class="fine">4172 Juniper Ridge Drive, Suite 517<br>Cedar Hollow, MI 48109<br>danielle.hartwell@brightpathoutcomes.example<br>www.brightpathoutcomes.example</p>
</section>

</body>
</html>
```